Local Computer Repair Business needs Flyer Design

I am looking for a small postcard sized (4x6) advertisement but use the full space 4x6. We are a local computer repair shop that provide sales and service of computer systems, any models, any problems. We also offer E-cycling for our customers. This will be distributed via post office box.
Emphasize shop locally, best service around, professional, Competitive prices.
One side for computer sales/repair and the other side should be E-Cycling. we'll receive old laptops, desktop computers, tablets, game consoles, etc..
Ad must include the attached logo.
Ad must include address - 247 Larkmoor Ave. Hudson, IA 50718
Ad must include phone number and website - 319-555-0427 and www.quorivapcworks.com

```html
<!DOCTYPE html>
<html lang="en">
<head>
<meta charset="utf-8">
<title>Quoriva PC Works – Postcard, Option 2</title>
<link rel="stylesheet" href="https://fonts.googleapis.com/css2?family=Oswald:wght@500;600;700&family=Lato:wght@400;700;900&display=swap">
<style>
  :root{
    --red:#d9222a;
    --blue:#2a56a8;
    --navy:#17295e;
    --white:#ffffff;
    --ink:#333a44;
    --stage:#3b3c3f;
    --rule:#9a9a9a;
    --photo-a:#7a5a3e;
    --photo-b:#c9b59c;
    --chip-a:#1c6b3a;
    --chip-b:#7cc24a;
  }
  *{box-sizing:border-box;margin:0;padding:0}
  html,body{width:902px;height:1200px;overflow:hidden}
  body{background:var(--stage);font-family:"Lato",sans-serif;position:relative;color:var(--ink)}
  .option-label{position:absolute;left:738px;top:124px;color:var(--white);font:700 16px "Lato",sans-serif;letter-spacing:.5px}

  .card{position:absolute;width:660px;height:440px;background:var(--white);overflow:hidden;box-shadow:0 8px 22px rgba(0,0,0,.45)}
  .card--front{left:60px;top:70px}
  .card--back{left:182px;top:650px}
  .card__art{position:absolute;inset:0}
  .abs{position:absolute}

  /* brand name stand-in */
  .brand{display:flex;align-items:center;gap:8px}
  .brand__dot{width:26px;height:26px;border-radius:50%;background:var(--blue)}
  .brand__name{font:900 17px/1.05 "Lato",sans-serif;color:var(--blue);letter-spacing:.5px}

  /* front */
  .front-brand{left:26px;top:30px}
  .front-banner{left:0;top:92px;width:334px;height:46px;background:var(--blue);clip-path:polygon(0 0,100% 0,94% 100%,0 100%);
    color:var(--white);font:600 27px/46px "Oswald",sans-serif;padding-left:22px;letter-spacing:.3px;white-space:nowrap}
  .front-lead{left:24px;top:148px;color:var(--blue);font:600 14px/1 "Oswald",sans-serif;white-space:nowrap}
  .front-hero{left:24px;top:167px;color:var(--red);font:700 26px/1 "Oswald",sans-serif;white-space:nowrap}
  .service-list{list-style:none;font:400 12.5px/1.35 "Lato",sans-serif;color:var(--ink)}
  .service-list li{position:relative;padding-left:14px;white-space:nowrap}
  .service-list li::before{content:"";position:absolute;left:0;top:6px;width:7px;height:7px;border-radius:50%;background:var(--red)}
  .services-a{left:30px;top:212px}
  .services-b{left:196px;top:212px}
  .badge{left:420px;top:250px;width:110px;height:110px;border-radius:50%;background:var(--red);color:var(--white);text-align:center;padding-top:21px;border:3px solid var(--white)}
  .badge__small{font:700 8px/1.1 "Lato",sans-serif;display:block}
  .badge__big{font:700 25px/1 "Oswald",sans-serif;display:block;margin-top:4px}
  .front-phone{left:26px;top:393px;color:var(--white);font:700 32px/1 "Lato",sans-serif;display:flex;align-items:center;gap:10px}
  .contact-lines{color:var(--white);font:400 13px/1.5 "Lato",sans-serif}
  .contact-lines p{display:flex;align-items:center;gap:7px;white-space:nowrap}
  .front-contact{left:378px;top:368px}

  /* back */
  .back-brand{left:370px;top:38px}
  .back-brand .brand__name{font-size:13px}
  .back-brand .brand__dot{width:20px;height:20px}
  .stamp-box{left:545px;top:28px;width:78px;height:78px;border:1px solid var(--rule)}
  .address-line{left:410px;width:215px;height:1px;background:var(--rule)}
  .ecycle-banner{left:0;top:48px;width:205px;height:42px;background:var(--red);clip-path:polygon(0 0,100% 0,92% 100%,0 100%);
    color:var(--white);font:700 31px/42px "Lato",sans-serif;padding-left:22px}
  .ecycle-head{left:24px;top:96px;color:var(--navy);font:700 24px/1 "Oswald",sans-serif}
  .ecycle-items{left:24px;top:124px;color:var(--red);font:700 15.5px/1.15 "Oswald",sans-serif}
  .ecycle-art{left:232px;top:30px;width:104px;height:92px;border-radius:10px;background:linear-gradient(135deg,var(--chip-a),var(--chip-b))}
  .ecycle-body{left:24px;top:168px;width:318px;font:400 8.6px/1.38 "Lato",sans-serif;color:var(--ink)}
  .ecycle-body p{margin-bottom:4px}
  .ecycle-body .call{color:var(--red);font-weight:900;margin-bottom:0}
  .ecycle-body .sub{color:var(--navy);font-weight:900;margin-bottom:1px}
  .back-phone{left:22px;top:378px;color:var(--white);font:700 22px/1 "Lato",sans-serif;display:flex;align-items:center;gap:6px}
  .back-contact{left:24px;top:402px;font-size:9.5px;line-height:1.4}
  .follow{left:270px;top:384px;color:var(--white);font:700 9.5px/1 "Lato",sans-serif;text-align:center}
  .follow__dots{display:flex;gap:6px;margin-top:6px;justify-content:center}
  .follow__dots span{width:17px;height:17px;border-radius:50%;background:var(--white)}
</style>
</head>
<body>
  <div class="option-label">OPTION 2</div>

  <!-- FRONT: repair side -->
  <section class="card card--front" aria-label="Computer repair side">
    <svg class="card__art" width="660" height="440" viewBox="0 0 660 440">
      <defs>
        <linearGradient id="workbench" x1="0" y1="0" x2="1" y2="1">
          <stop offset="0" stop-color="var(--photo-a)"/>
          <stop offset="1" stop-color="var(--photo-b)"/>
        </linearGradient>
        <linearGradient id="thumb" x1="0" y1="0" x2="1" y2="1">
          <stop offset="0" stop-color="#2f6fb5"/>
          <stop offset="1" stop-color="#a9c2db"/>
        </linearGradient>
      </defs>
      <circle cx="600" cy="62" r="248" fill="var(--red)"/>
      <circle cx="600" cy="62" r="240" fill="var(--blue)"/>
      <circle cx="600" cy="62" r="234" fill="var(--white)"/>
      <circle cx="600" cy="62" r="229" fill="url(#workbench)" role="img" aria-label="Photo of hands repairing a motherboard beside a laptop on a wooden desk"/>
      <polygon points="330,340 660,340 660,440 290,440" fill="var(--navy)"/>
      <polygon points="0,384 352,384 318,440 0,440" fill="var(--red)"/>
      <g stroke="var(--blue)" stroke-width="4" fill="url(#thumb)">
        <circle cx="64" cy="322" r="30" role="img" aria-label="Photo of desktop tower repair"/>
        <circle cx="134" cy="316" r="30" role="img" aria-label="Photo of laptops"/>
        <circle cx="204" cy="310" r="30" role="img" aria-label="Image of virus protection"/>
        <circle cx="274" cy="304" r="30" role="img" aria-label="Photo of keyboard and hardware"/>
        <circle cx="344" cy="298" r="30" role="img" aria-label="Image of network cables"/>
      </g>
    </svg>

    <div class="abs brand front-brand"><span class="brand__dot"></span><span class="brand__name">QUORIVA PC WORKS,<br>LLC</span></div>
    <h1 class="abs front-banner">COMPUTER REPAIR SHOP</h1>
    <p class="abs front-lead">PROVIDE SALES AND SERVICE OF COMPUTER SYSTEMS,</p>
    <p class="abs front-hero">ANY MODELS, ANY PROBLEMS</p>
    <ul class="abs service-list services-a">
      <li>Repairs/Upgrades</li>
      <li>Custom Computers</li>
      <li>Laptop Screen Repair</li>
    </ul>
    <ul class="abs service-list services-b">
      <li>Virus and Malware Removal</li>
      <li>Software Installations<br>and Configuration</li>
    </ul>
    <div class="abs badge">
      <span class="badge__small">MOST REPAIRS CAN<br>BE COMPLETED IN</span>
      <span class="badge__big">24/48<br>HRS</span>
    </div>
    <p class="abs front-phone">
      <svg width="26" height="26" viewBox="0 0 26 26"><circle cx="13" cy="13" r="11.5" fill="none" stroke="var(--white)" stroke-width="2"/><path d="M9 7l3 3-1.5 2a8 8 0 0 0 4 4l2-1.5 3 3-2 2c-5 0-10.5-5.5-10.5-10.5z" fill="var(--white)"/></svg>
      319-555-0427
    </p>
    <div class="abs contact-lines front-contact">
      <p><svg width="10" height="13" viewBox="0 0 10 13"><path d="M5 0a5 5 0 0 1 5 5c0 3.5-5 8-5 8S0 8.5 0 5a5 5 0 0 1 5-5z" fill="var(--white)"/><circle cx="5" cy="5" r="1.8" fill="var(--navy)"/></svg>247 Larkmoor Ave. Hudson, IA 50718</p>
      <p><svg width="11" height="11" viewBox="0 0 12 12"><circle cx="6" cy="6" r="5.2" fill="none" stroke="var(--white)" stroke-width="1.3"/><path d="M1 6h10M6 1c-2.5 3-2.5 7 0 10M6 1c2.5 3 2.5 7 0 10" fill="none" stroke="var(--white)" stroke-width="1"/></svg>www.quorivapcworks.com</p>
    </div>
  </section>

  <!-- BACK: e-cycling + mailing side -->
  <section class="card card--back" aria-label="E-cycling side">
    <svg class="card__art" width="660" height="440" viewBox="0 0 660 440">
      <path d="M300 0 Q395 190 352 440" fill="none" stroke="var(--red)" stroke-width="12"/>
      <path d="M318 0 Q412 190 366 440" fill="none" stroke="var(--navy)" stroke-width="5"/>
      <path d="M0 372 L340 360 Q348 400 352 440 L0 440 Z" fill="var(--navy)"/>
    </svg>

    <div class="abs brand back-brand"><span class="brand__dot"></span><span class="brand__name">QUORIVA PC WORKS,<br>LLC</span></div>
    <div class="abs stamp-box"></div>
    <div class="abs address-line" style="top:210px"></div>
    <div class="abs address-line" style="top:250px"></div>
    <div class="abs address-line" style="top:290px"></div>

    <h2 class="abs ecycle-banner">E-CYCLING</h2>
    <div class="abs ecycle-art" role="img" aria-label="Recycling arrows illustration filled with circuit board texture"></div>
    <p class="abs ecycle-head">WE'LL RECEIVE OLD</p>
    <p class="abs ecycle-items">LAPTOPS, DESKTOP COMPUTERS,<br>TABLETS, GAME CONSOLES, ETC..</p>

    <div class="abs ecycle-body">
      <p>According the WEDC (World Electronics Data Council), there was over 44.7 million metric tonnes of e-waste generated in 2017 and much of that waste was not properly disposed of.</p>
      <p>Many people are unaware of the various hazardous substances that can be found in our everyday electronics. These hazardous and toxic materials become harmful to our health as well as the environment when not disposed of properly. Our E-Cycling process follows government guidelines to ensure safe disposal.</p>
      <p class="call">SO WHEN IT'S TIME TO REPLACE YOUR OLD OR BROKEN ELECTRONICS, GIVE US A CALL</p>
      <p class="sub">DATA DESTRUCTION (OPTIONAL)</p>
      <p>Quoriva PC Works does offer data destruction as part of our recycling process. This option does have a fee associated with it. If you are interested in data destruction just let us know when you contact us for recycling. If you have a business we do offer data destruction on-site, contact us for a quote.</p>
    </div>

    <p class="abs back-phone">
      <svg width="18" height="18" viewBox="0 0 26 26"><circle cx="13" cy="13" r="11.5" fill="none" stroke="var(--white)" stroke-width="2"/><path d="M9 7l3 3-1.5 2a8 8 0 0 0 4 4l2-1.5 3 3-2 2c-5 0-10.5-5.5-10.5-10.5z" fill="var(--white)"/></svg>
      319-555-0427
    </p>
    <div class="abs contact-lines back-contact">
      <p><svg width="8" height="11" viewBox="0 0 10 13"><path d="M5 0a5 5 0 0 1 5 5c0 3.5-5 8-5 8S0 8.5 0 5a5 5 0 0 1 5-5z" fill="var(--white)"/><circle cx="5" cy="5" r="1.8" fill="var(--navy)"/></svg>247 Larkmoor Ave. Hudson, IA 50718</p>
      <p><svg width="9" height="9" viewBox="0 0 12 12"><circle cx="6" cy="6" r="5.2" fill="none" stroke="var(--white)" stroke-width="1.3"/><path d="M1 6h10M6 1c-2.5 3-2.5 7 0 10M6 1c2.5 3 2.5 7 0 10" fill="none" stroke="var(--white)" stroke-width="1"/></svg>www.quorivapcworks.com</p>
    </div>
    <div class="abs follow">
      FOLLOW US ON
      <div class="follow__dots"><span></span><span></span><span></span></div>
    </div>
  </section>
</body>
</html>
```